Mark Dunvale actor business cards

I need unique and interesting business cards that have my headshot photo, my name, tagline/position/skills, contact info, preferred pronouns (he, him, his), and social media handles. These need to be memorable networking tools to hand out at events that stand out. I am an actor that works in theatre, film, and TV and usually play darker dramatic roles, though it doesn't have to necessarily need to be reflected in the design, but I am not a light, comedic actor. In my email tagline, My position/skills are "Actor, storyteller, theatre maker."

Target Market(s)

Casting directors, film and television community, theatre community.

Industry/Entity Type

Performing Art

Contact Information for Business Card

Mark Dunvale. Pronouns: he, him, his. Contact info: (555)-318-7406, Markdunvale.example, markdunvale@mailbox.example. Talent representation: Corvanti Talent Agency. Social Media: Friendbook page, chirpit and snapgram: @MarkDunvaleActs. Company Member of Larkhollow Theatre Company.

Font styles to use
Serif
Decorative

Colors

Designer to choose colors to be used in the design.

Requirements
Must have
• Headshot photo, name, tagline, preferred pronouns, contact info, Social media handle, talent agency logo, larkhollow theatre company logo. Both logos should be smaller than my name. Under or near Larkhollow logo, it should say "Company Member"
Nice to have
• I would like to have the photo, my name, tagline, and maybe pronouns on one side, and all contact info, and social media, and talent agency logo on the other. I would like the style to reflect my type which is a little more serious and somewhat darker, and definitely not comedic.
Should not have
• No extraneous theatre lights, camera, or film, etc. clip art or photos. Use solid backgrounds or photos provided.

```html
<!DOCTYPE html>
<html lang="en">
<head>
<meta charset="utf-8">
<title>Mark Dunvale — Actor Business Cards</title>
<link rel="stylesheet" href="https://fonts.googleapis.com/css2?family=Bodoni+Moda:opsz,wght@6..96,500&family=Courier+Prime:wght@400;700&display=swap">
<style>
  :root {
    --backdrop: #b9b9b9;
    --card-dark: #262626;
    --ink-light: #f4f4f4;
    --ink-soft: #d6d6d6;
    --name-yellow: #f2e21a;
    --logo-ink: #1c1c1c;
    --photo-light: #a9a9a9;
    --photo-mid: #6f6f6f;
    --photo-deep: #3a3a3a;
  }
  * { margin: 0; padding: 0; box-sizing: border-box; }
  html, body { width: 1200px; height: 1000px; overflow: hidden; }
  body {
    background: var(--backdrop);
    display: flex;
    align-items: center;
    justify-content: center;
    gap: 60px;
  }
  .card {
    position: relative;
    width: 440px;
    height: 770px;
    overflow: hidden;
    box-shadow: 0 6px 18px rgba(0,0,0,0.35);
  }
  /* Front */
  .headshot {
    position: absolute; inset: 0;
    background:
      radial-gradient(ellipse 55% 40% at 55% 38%, var(--photo-light), transparent 70%),
      linear-gradient(180deg, var(--photo-mid) 0%, var(--photo-mid) 55%, var(--photo-deep) 100%);
  }
  .name {
    position: absolute;
    left: 38px; top: 510px;
    font-family: "Bodoni Moda", "Didot", serif;
    font-weight: 500;
    color: var(--name-yellow);
    line-height: 0.95;
  }
  .name-first { display: block; font-size: 64px; }
  .name-last { display: block; font-size: 62px; letter-spacing: 1px; }
  .pronouns {
    position: absolute;
    left: 0; right: 0; top: 655px;
    text-align: center;
    font-family: "Courier Prime", "Courier New", monospace;
    font-size: 26px;
    color: var(--ink-light);
  }
  .tagline {
    position: absolute;
    left: 0; right: 0; top: 705px;
    text-align: center;
    font-family: "Courier Prime", "Courier New", monospace;
    font-size: 18px;
    letter-spacing: 0.5px;
    color: var(--ink-soft);
  }
  /* Back */
  .card-back { background: var(--card-dark); }
  .back-portrait {
    position: absolute; inset: 0;
    background: linear-gradient(100deg, #3d3d3d 0%, #2f2f2f 45%, var(--card-dark) 70%);
  }
  .agency-mark {
    position: absolute;
    right: 40px; top: 100px;
    width: 140px; height: 140px;
    border-radius: 50%;
    background: #ffffff;
    display: flex; flex-direction: column;
    align-items: center; justify-content: center;
    font-family: "Courier Prime", "Courier New", monospace;
    color: var(--logo-ink);
  }
  .agency-mark-name { font-size: 22px; }
  .agency-mark-sub { font-size: 9px; margin-top: 2px; }
  .contact {
    position: absolute;
    right: 40px; top: 270px;
    text-align: right;
    font-family: "Courier Prime", "Courier New", monospace;
    font-size: 25px;
    line-height: 1.22;
    color: var(--ink-light);
  }
  .contact p + p { margin-top: 14px; }
  .contact .email { font-size: 21px; }
  .company-member {
    position: absolute;
    right: 40px; top: 560px;
    display: flex; align-items: center; gap: 12px;
    font-family: "Courier Prime", "Courier New", monospace;
    color: var(--ink-light);
    text-align: right;
  }
  .company-member-square {
    width: 34px; height: 34px;
    background: var(--ink-light);
    flex-shrink: 0;
  }
  .company-member-name { font-size: 17px; line-height: 1.2; }
  .company-member-label { font-size: 14px; color: var(--ink-soft); margin-top: 2px; }
  .social {
    position: absolute;
    left: 0; right: 40px; top: 665px;
    text-align: right;
    font-family: "Courier Prime", "Courier New", monospace;
    color: var(--ink-light);
  }
  .social-networks { font-size: 18px; letter-spacing: 1px; }
  .social-handle { font-size: 24px; font-weight: 700; margin-top: 14px; }
</style>
</head>
<body>
  <section class="card card-front">
    <div class="headshot" role="img" aria-label="Black and white headshot of Mark Dunvale smiling, wearing a grey button-up shirt"></div>
    <h1 class="name"><span class="name-first">Mark</span><span class="name-last">DUNVALE</span></h1>
    <p class="pronouns">he, him, his</p>
    <p class="tagline">Actor, storyteller, theatre maker</p>
  </section>

  <section class="card card-back">
    <div class="back-portrait" role="img" aria-label="Darkened close-up of Mark Dunvale's face, fading into black"></div>
    <div class="agency-mark">
      <span class="agency-mark-name">Corvanti</span>
      <span class="agency-mark-sub">Talent Agency</span>
    </div>
    <div class="contact">
      <p>Contact info:<br>(555)-318-7406</p>
      <p>Markdunvale.example<br><span class="email">markdunvale@mailbox.example</span></p>
      <p>Talent representation:<br>Corvanti Talent Agency</p>
    </div>
    <div class="company-member">
      <div>
        <p class="company-member-name">Larkhollow Theatre Company</p>
        <p class="company-member-label">Company Member</p>
      </div>
      <span class="company-member-square"></span>
    </div>
    <div class="social">
      <p class="social-networks">Friendbook · snapgram · chirpit</p>
      <p class="social-handle">@MarkDunvaleActs</p>
    </div>
  </section>
</body>
</html>
```